Packaging Design of Home Decor Retail Box Front

Looking to refresh a Home Decor Package Box Front for Mass Retail Placement
Box size is 26.25" wide by 17.5" High
Must have Roomquill logo.
Must say "10 Piece Frame Set"
Must say "Easily hangs with 4 nails"
Product should be shown in room scene - room scene can be found on any royalty free online site - can show with water mark.
Room should be aspirational and on trend, and show product as large as possible.
Room scene should complement the design of the product.

Target Market(s)

Shoppers at Mass Retail that are looking for Wall Decor. They are looking to make a statement with a large and easy to hang wall decor set.

Industry/Entity Type

Home Furnishing

Font styles to use
Serif
Sans Serif

Colors

Designer to choose colors to be used in the design.

Requirements
Must have
• Box size is 26.25" wide by 17.5" High
• Must have Roomquill logo.
• Must say "10 Piece Frame Set"
• Must say "Easily hangs with 4 nails"
• Product should be shown in room scene - room scene can be found on any royalty free online site - can show with water mark.
• Room should be aspirational and on trend, and show product as large as possible.
• Room scene should complement the design of the product.
Nice to have
• Look at history of old box sets to see where we have been before. - PDF
• Ideally pick a room where you would see this product displayed in a home.
Should not have
• Room scene should not have people.
• Do not duplicate what we have done before - needs to be the next generation of where we have been; but fresher, cleaner. Text and layout should be more modern. Room scene should match the product feel, however.
• Do not add extra verbiage.

```html
<!DOCTYPE html>
<html lang="en">
<head>
<meta charset="utf-8">
<title>Roomquill 10 Piece Frame Set – Box Front</title>
<link rel="stylesheet" href="https://fonts.googleapis.com/css2?family=Oswald:wght@400;500&family=Cinzel:wght@700&family=Open+Sans:wght@400;600&display=swap">
<style>
  :root {
    --wall: #ecebe8;
    --ink: #111111;
    --paper: #ffffff;
    --badge-grey: #a9a9a9;
    --sign-text: #8c8c8c;
    --frame: #dcdcdc;
    --frame-edge: #c9c9c9;
    --mat: #f3f3f3;
    --rope: #c8ab7c;
    --mantel: #9b8570;
    --brick: #e4e3e0;
  }
  * { margin: 0; padding: 0; box-sizing: border-box; }
  html, body { width: 1200px; height: 785px; overflow: hidden; background: var(--wall); }
  .box-front { position: relative; width: 1200px; height: 785px; overflow: hidden; }
  .room-scene { position: absolute; inset: 0; }
  .brand-panel {
    position: absolute; left: 30px; top: 54px; width: 337px; height: 127px;
    background: var(--paper);
    display: flex; align-items: center; justify-content: center; gap: 14px;
  }
  .brand-mark { width: 18px; height: 18px; background: var(--ink); }
  .brand-name {
    font-family: "Open Sans", sans-serif; font-weight: 600;
    font-size: 46px; line-height: 1; color: var(--ink);
  }
  .piece-badge { position: absolute; left: 112px; top: 522px; width: 166px; }
  .piece-badge__count {
    height: 128px; background: var(--ink); color: var(--paper);
    font-family: "Oswald", sans-serif; font-weight: 500; font-size: 104px;
    line-height: 128px; text-align: center;
  }
  .piece-badge__label {
    height: 51px; background: var(--badge-grey); color: var(--paper);
    font-family: "Oswald", sans-serif; font-weight: 400; font-size: 22px;
    line-height: 51px; text-align: center;
  }
  .hang-note {
    position: absolute; left: 99px; top: 731px;
    font-family: "Open Sans", sans-serif; font-size: 16px; color: var(--ink);
  }
  .sign-title { font-family: "Cinzel", serif; font-weight: 700; }
</style>
</head>
<body>
<main class="box-front">
  <svg class="room-scene" width="1200" height="785" viewBox="0 0 1200 785">
    <defs>
      <linearGradient id="wallTone" x1="0" y1="0" x2="1" y2="1">
        <stop offset="0" stop-color="#e6e5e2"/>
        <stop offset="0.5" stop-color="#f4f3f1"/>
        <stop offset="1" stop-color="#e9e8e5"/>
      </linearGradient>
    </defs>
    <rect class="wall" width="1200" height="785" fill="url(#wallTone)" role="img" aria-label="Bright white living room wall with ceiling beams"/>
    <rect class="ceiling-beam" x="0" y="0" width="1200" height="40" fill="#f1f0ee"/>

    <rect class="mantel-shelf" x="326" y="636" width="874" height="40" fill="var(--mantel)" role="img" aria-label="Rustic wooden mantel shelf"/>
    <rect class="fireplace" x="376" y="676" width="776" height="109" fill="var(--brick)" role="img" aria-label="White painted brick fireplace"/>

    <g class="hanger">
      <polyline points="416,166 774,61 1140,166" fill="none" stroke="var(--rope)" stroke-width="3"/>
      <circle cx="774" cy="63" r="11" fill="#cfcfcf" stroke="#b8b8b8" stroke-width="2"/>
    </g>

    <g class="sign-board">
      <rect x="406" y="164" width="743" height="86" fill="#efefee" stroke="#d9d9d9"/>
      <text class="sign-title" x="440" y="232" font-size="58" textLength="680" lengthAdjust="spacingAndGlyphs" fill="var(--sign-text)">FAMILY TREE</text>
    </g>

    <g class="hanging-wires" stroke="#bdbdbd" stroke-width="1.5">
      <line x1="467" y1="250" x2="467" y2="264"/>
      <line x1="629" y1="250" x2="629" y2="264"/>
      <line x1="776" y1="250" x2="776" y2="266"/>
      <line x1="924" y1="250" x2="924" y2="264"/>
      <line x1="1088" y1="250" x2="1088" y2="264"/>
      <line x1="629" y1="373" x2="629" y2="394"/>
      <line x1="776" y1="344" x2="776" y2="366"/>
      <line x1="924" y1="373" x2="924" y2="394"/>
      <line x1="776" y1="474" x2="776" y2="496"/>
    </g>

    <g class="frames" stroke="var(--frame-edge)" stroke-width="1">
      <rect x="404" y="264" width="126" height="155" fill="var(--frame)"/>
      <rect x="414" y="274" width="106" height="135" fill="var(--mat)"/>
      <rect x="438" y="298" width="59" height="89" fill="#c29a7f" role="img" aria-label="Photo of a child holding a pet rabbit"/>

      <rect x="590" y="264" width="78" height="109" fill="var(--frame)"/>
      <rect x="601" y="274" width="58" height="88" fill="#5f7a45" role="img" aria-label="Photo of a golden retriever on grass"/>

      <rect x="722" y="266" width="107" height="78" fill="var(--frame)"/>
      <rect x="733" y="277" width="89" height="58" fill="#a99f86" role="img" aria-label="Photo of a family relaxing together"/>

      <rect x="886" y="264" width="77" height="109" fill="var(--frame)"/>
      <rect x="896" y="274" width="58" height="88" fill="#6f8a86" role="img" aria-label="Photo of a father and child at the coast"/>

      <rect x="1026" y="264" width="125" height="155" fill="var(--frame)"/>
      <rect x="1036" y="274" width="105" height="135" fill="var(--mat)"/>
      <rect x="1058" y="298" width="58" height="89" fill="#8a9a66" role="img" aria-label="Photo of a grandmother sitting outdoors with a bicycle"/>

      <rect x="568" y="394" width="125" height="154" fill="var(--frame)"/>
      <rect x="578" y="404" width="105" height="134" fill="var(--mat)"/>
      <rect x="594" y="419" width="73" height="104" fill="#6c7450" role="img" aria-label="Photo of a mother holding her toddler"/>

      <rect x="738" y="366" width="78" height="108" fill="var(--frame)"/>
      <rect x="747" y="376" width="59" height="88" fill="#4f5c4a" role="img" aria-label="Photo of two brothers smiling"/>

      <rect x="863" y="394" width="124" height="154" fill="var(--frame)"/>
      <rect x="873" y="404" width="104" height="134" fill="var(--mat)"/>
      <rect x="887" y="419" width="74" height="104" fill="#a7ab86" role="img" aria-label="Photo of children playing on a beach"/>

      <rect x="730" y="496" width="93" height="124" fill="var(--frame)"/>
      <rect x="742" y="506" width="72" height="104" fill="#7f988d" role="img" aria-label="Photo of a family on porch steps"/>
    </g>
  </svg>

  <div class="brand-panel">
    <span class="brand-mark"></span>
    <span class="brand-name">Roomquill</span>
  </div>

  <div class="piece-badge">
    <div class="piece-badge__count">10</div>
    <div class="piece-badge__label">Pieces Frame set</div>
  </div>

  <p class="hang-note">Easily hangs with 4 nails</p>
</main>
</body>
</html>
```